I need to rebrand my public user portal for a new/modern look and feel

I want to take my current user web portal and redesign the look of it. I have included 2 samples of my current user portal and would like options to create a new functional look. This main page below will modify based on the tabs on the top left. Any questions please ask.

```html
<!DOCTYPE html>
<html lang="en">
<head>
<meta charset="utf-8">
<title>Student Dashboard</title>
<link href="https://fonts.googleapis.com/css2?family=Nunito:wght@400;500;600;700&display=swap" rel="stylesheet">
<style>
:root{
  --page:#0c1627;
  --header:#182c4e;
  --card:#ffffff;
  --ink:#1f2430;
  --muted:#8a8f99;
  --primary:#2f6fc4;
  --primary-soft:#dbe7f6;
  --row-line:#e6e8ec;
  --head-bg:#f8f9fb;
  --empty-bg:#eef2f7;
  --danger:#e04848;
  --field:#f0f1f3;
}
*{box-sizing:border-box;margin:0;padding:0}
html,body{width:1200px;height:853px;overflow:hidden}
body{background:var(--page);font-family:'Nunito',sans-serif;color:var(--ink);position:relative}
.topbar{position:absolute;left:0;top:0;width:1200px;height:83px;background:var(--header)}
.brand{position:absolute;left:73px;top:30px;display:flex;align-items:center;gap:8px;color:#fff;font-weight:700;font-size:15px}
.brand-dot{width:22px;height:22px;border-radius:50%;background:#fff}
.nav{position:absolute;top:28px;display:flex;align-items:center;gap:8px;color:#fff;font-size:12.5px;height:33px}
.nav svg{width:18px;height:18px;fill:none;stroke:#fff;stroke-width:1.6}
.nav.active{left:317px;width:110px;background:var(--primary);border-radius:17px;padding-left:14px}
.nav.active svg{fill:#fff;stroke:none}
.user{position:absolute;left:1040px;top:37px;color:#fff;font-size:12.5px}
.bell{position:absolute;left:997px;top:34px;width:18px;height:18px;fill:none;stroke:#fff;stroke-width:1.6}
.avatar{position:absolute;left:1100px;top:27px;width:35px;height:35px;border-radius:50%;background:linear-gradient(135deg,#b9a79c,#4b3a36)}
.caret{position:absolute;left:1141px;top:41px;border-left:4px solid transparent;border-right:4px solid transparent;border-top:7px solid #fff}
.card{position:absolute;left:166px;width:887px;background:var(--card);border-radius:4px}
.card-title{position:absolute;left:46px;top:40px;font-size:17px;font-weight:500}
.search{position:absolute;left:399px;top:30px;width:247px;height:40px;background:var(--field);border-radius:8px;display:flex;align-items:center;padding-left:14px;gap:10px;color:var(--muted);font-size:12px}
.search svg{width:18px;height:18px;fill:none;stroke:#888;stroke-width:1.8}
.filter{position:absolute;left:670px;top:30px;height:40px;display:flex;align-items:center;gap:9px;font-size:12px}
.add-btn{position:absolute;left:740px;top:30px;width:121px;height:40px;background:var(--primary);border-radius:3px;color:#fff;font-size:12px;display:flex;align-items:center;justify-content:center;gap:9px}
.table{position:absolute;left:27px;top:91px;width:850px}
.row{position:relative;height:36px;border-bottom:1px solid var(--row-line);font-size:11.5px}
.row.head{height:36px;background:var(--head-bg);font-weight:500;font-size:12px}
.row span{position:absolute;top:50%;transform:translateY(-50%)}
.c-name{left:88px}.c-grade{left:394px}.c-year{left:497px}.c-school{left:607px}
.check{position:absolute;left:25px;top:50%;transform:translateY(-50%);width:17px;height:17px;border:1.5px solid #333;border-radius:4px}
.check.on{background:var(--primary);border-color:var(--primary)}
.kebab{position:absolute;left:806px;top:50%;transform:translateY(-50%);width:18px;height:18px;border:1px solid var(--row-line);border-radius:3px;display:flex;flex-direction:column;align-items:center;justify-content:center;gap:2px}
.kebab i{width:2px;height:2px;background:#333;border-radius:1px}
.kebab.open{background:var(--primary-soft);border-color:var(--primary-soft)}
.empty{height:97px;background:var(--empty-bg);display:flex;flex-direction:column;align-items:center;justify-content:center;gap:10px;font-size:12px}
.empty svg{width:29px;height:29px}
.menu{position:absolute;left:957px;top:300px;width:102px;height:100px;background:#fff;border-radius:4px;box-shadow:0 2px 8px rgba(0,0,0,.15);z-index:5;padding:15px 0 0 19px;font-size:12px}
.menu div{display:flex;align-items:center;gap:8px;height:27px;color:var(--primary)}
.menu div.del{color:var(--danger)}
.menu svg{width:14px;height:14px;fill:none;stroke:currentColor;stroke-width:1.7}
</style>
</head>
<body>
<header class="topbar">
  <div class="brand"><span class="brand-dot"></span>Northgate Portal</div>
  <div class="nav active"><svg viewBox="0 0 24 24"><path d="M12 3 2 12h3v9h5v-6h4v6h5v-9h3z"/></svg>Dashboard</div>
  <div class="nav" style="left:460px"><svg viewBox="0 0 24 24"><rect x="6" y="4" width="12" height="16" rx="1"/><path d="M3 6v12M21 6v12"/></svg>Application</div>
  <div class="nav" style="left:579px"><svg viewBox="0 0 24 24"><path d="M6 2h8l5 5v15H6z"/><path d="M14 2v5h5"/></svg>Transcipt Request</div>
  <div class="nav" style="left:742px"><svg viewBox="0 0 24 24"><rect x="4" y="10" width="16" height="11" rx="1"/><path d="M5 6h14M7 3h10M4 14h16"/></svg>New Hire Packet</div>
  <svg class="bell" viewBox="0 0 24 24"><path d="M6 17V11a6 6 0 0 1 12 0v6l2 2H4zM10 21h4"/></svg>
  <div class="user">Maren L</div>
  <div class="avatar" role="img" aria-label="User profile photo"></div>
  <div class="caret"></div>
</header>

<section class="card" style="top:107px;height:270px">
  <h2 class="card-title">SCSSDEMO19</h2>
  <div class="search"><svg viewBox="0 0 24 24"><circle cx="10.5" cy="10.5" r="7"/><path d="m16 16 5 5"/></svg>Search</div>
  <div class="filter"><svg width="14" height="10" viewBox="0 0 14 10"><path d="M0 1h14M3 5h8M5 9h4" stroke="#222" stroke-width="1.6"/></svg>Filter</div>
  <div class="add-btn"><svg width="18" height="18" viewBox="0 0 18 18"><path d="M9 1v16M1 9h16" stroke="#fff" stroke-width="1.8"/></svg>Add Student</div>
  <div class="table">
    <div class="row head"><i class="check"></i><span class="c-name">Name</span><span class="c-grade">Grade</span><span class="c-year">Year</span><span class="c-school">School</span></div>
    <div class="row"><i class="check on"><svg viewBox="0 0 16 16" width="14" height="14"><path d="M4 8l3 3 5-6" stroke="#fff" stroke-width="2" fill="none"/></svg></i><span class="c-name">Maren Lindqvist</span><span class="c-grade">10</span><span class="c-year">2025</span><span class="c-school">Ridgeview High School</span><div class="kebab"><i></i><i></i><i></i></div></div>
    <div class="row"><i class="check"></i><span class="c-name">Dorian Pike</span><span class="c-grade">08</span><span class="c-year">2025</span><span class="c-school">Ridgeview High School</span><div class="kebab open"><i></i><i></i><i></i></div></div>
    <div class="row"><i class="check"></i><span class="c-name">Elliot Warde</span><span class="c-grade">08</span><span class="c-year">2025</span><span class="c-school">Ridgeview High School</span></div>
  </div>
</section>

<div class="menu">
  <div><svg viewBox="0 0 24 24"><path d="M4 20h16M6 16l10-10 3 3-10 10H6z"/></svg>Edit</div>
  <div><svg viewBox="0 0 24 24"><rect x="3" y="4" width="18" height="16" rx="2"/><path d="M3 9h18M9 13h6"/></svg>Archive</div>
  <div class="del"><svg viewBox="0 0 24 24"><path d="M4 6h16M9 6V3h6v3M6 6l1 15h10l1-15"/></svg>Delete</div>
</div>

<section class="card" style="top:390px;height:254px">
  <h2 class="card-title">County Vocational School</h2>
  <div class="search"><svg viewBox="0 0 24 24"><circle cx="10.5" cy="10.5" r="7"/><path d="m16 16 5 5"/></svg>Search</div>
  <div class="filter"><svg width="14" height="10" viewBox="0 0 14 10"><path d="M0 1h14M3 5h8M5 9h4" stroke="#222" stroke-width="1.6"/></svg>Filter</div>
  <div class="add-btn"><svg width="18" height="18" viewBox="0 0 18 18"><path d="M9 1v16M1 9h16" stroke="#fff" stroke-width="1.8"/></svg>Add Student</div>
  <div class="table">
    <div class="row head"><i class="check"></i><span class="c-name">Name</span><span class="c-grade">Grade</span><span class="c-year">Year</span><span class="c-school">School</span></div>
    <div class="empty"><svg viewBox="0 0 30 30"><circle cx="15" cy="15" r="13" fill="none" stroke="#2f6fc4" stroke-width="2.4"/><path d="M15 8v9" stroke="#2f6fc4" stroke-width="2.6"/><circle cx="15" cy="21.5" r="1.6" fill="#2f6fc4"/></svg>No students found. Please add a new student.</div>
  </div>
</section>

<section class="card" style="top:658px;height:254px">
  <h2 class="card-title">Progress Demo School</h2>
  <div class="search"><svg viewBox="0 0 24 24"><circle cx="10.5" cy="10.5" r="7"/><path d="m16 16 5 5"/></svg>Search</div>
  <div class="filter"><svg width="14" height="10" viewBox="0 0 14 10"><path d="M0 1h14M3 5h8M5 9h4" stroke="#222" stroke-width="1.6"/></svg>Filter</div>
  <div class="add-btn"><svg width="18" height="18" viewBox="0 0 18 18"><path d="M9 1v16M1 9h16" stroke="#fff" stroke-width="1.8"/></svg>Add Student</div>
  <div class="table">
    <div class="row head"><i class="check"></i><span class="c-name">Name</span><span class="c-grade">Grade</span><span class="c-year">Year</span><span class="c-school">School</span></div>
    <div class="empty"><svg viewBox="0 0 30 30"><circle cx="15" cy="15" r="13" fill="none" stroke="#2f6fc4" stroke-width="2.4"/><path d="M15 8v9" stroke="#2f6fc4" stroke-width="2.6"/><circle cx="15" cy="21.5" r="1.6" fill="#2f6fc4"/></svg>No students found. Please add a new student.</div>
  </div>
</section>
</body>
</html>
```